Accident Law Firm Billboard Bold Easy to See Car Accidents

We need a billboard design that can catch attention in a very crowed Car Accident lawyer market. We wish to feature the phone number (407) 555-0148 as the focus of the Bill Board. We are trying to get the phone number recognized and remembered by drivers. The law firm name is not as crucial to remember.
Basically, It's CAR ACCIDENT? Then (407) 555-0148. We are not married to any specific color scheme but it has to POP and catch attention.
So the Crucial elements are as follows:
1. Phone number (407) 555-0148
2. Words CAR ACCIDENT?
3. Firm Logo in lower portion or where appropriate. Firm Logo to be provided
4. We may want to try a Day Glow orange color, with White and Black added. An example of the color scheme shall be provided.
5. Possible "Catch Phrase" to be used, "It's Time Call 9"
Target Market(s)
Orlando Florida Car Accident victims
Industry/Entity Type
Law Firm
Requirements
Must have
- Easy to see phone number (407) 555-0148
- Catch attention
Nice to have
- I would like to have the sign visible in bright sunlight and it not too hard to immediately know what phone number is for
Should not have
- too many words
- No bold enough
- confusing fonts
- Unclear fonts

```html
<!DOCTYPE html>
<html lang="en">
<head>
<meta charset="utf-8">
<title>Marvella Law Firm P.C. – Car Accident Billboard</title>
<link rel="stylesheet" href="https://fonts.googleapis.com/css2?family=Barlow+Semi+Condensed:wght@700;800&display=swap">
<style>
  :root {
    --frame: #3a3a3c;
    --board: #f7f8f8;
    --ink: #161616;
    --dayglow: #f15a29;
    --orange-soft: #f6894a;
    --orange-light: #f8a064;
    --photo-sky: #6f8a3c;
    --photo-foliage: #2f4a22;
    --photo-road: #3c3d3f;
    --photo-car: #111214;
  }
  html, body {
    margin: 0;
    padding: 0;
    width: 1200px;
    height: 413px;
    overflow: hidden;
    background: var(--frame);
  }
  .billboard {
    position: relative;
    width: 1200px;
    height: 413px;
    background: var(--frame);
  }
  .board {
    position: absolute;
    left: 54px;
    top: 54px;
    width: 1092px;
    height: 305px;
    background: var(--board);
    overflow: hidden;
  }
  .board-art {
    position: absolute;
    inset: 0;
    width: 1092px;
    height: 305px;
  }
  .message {
    position: absolute;
    left: 0;
    top: 0;
    width: 620px;
    height: 305px;
    text-align: center;
    font-family: "Barlow Semi Condensed", "Arial Narrow", sans-serif;
  }
  .firm-name {
    position: absolute;
    left: 0;
    right: 0;
    top: 36px;
    margin: 0;
    font-weight: 700;
    font-size: 34px;
    line-height: 1;
    letter-spacing: 2px;
    color: var(--ink);
  }
  .headline {
    position: absolute;
    left: 0;
    right: 0;
    top: 116px;
    margin: 0;
    font-weight: 800;
    font-size: 80px;
    line-height: 1;
    letter-spacing: 0.5px;
    color: var(--ink);
  }
  .phone {
    position: absolute;
    left: 0;
    right: 0;
    top: 190px;
    margin: 0;
    font-weight: 800;
    font-size: 72px;
    line-height: 1;
    letter-spacing: 1px;
    color: var(--dayglow);
    text-decoration: none;
    display: block;
  }
</style>
</head>
<body>
  <div class="billboard">
    <div class="board">
      <svg class="board-art" viewBox="0 0 1092 305" aria-hidden="false">
        <defs>
          <linearGradient id="photo-tones" x1="0" y1="0" x2="0" y2="1">
            <stop offset="0" stop-color="var(--photo-sky)"/>
            <stop offset="0.3" stop-color="var(--photo-foliage)"/>
            <stop offset="0.5" stop-color="var(--photo-road)"/>
            <stop offset="1" stop-color="var(--photo-car)"/>
          </linearGradient>
        </defs>
        <path class="orange-wave" d="M714 0 C 660 90, 610 200, 582 305 L 810 305 L 810 0 Z" fill="var(--orange-soft)"/>
        <path class="orange-wave-light" d="M735 0 C 690 110, 650 210, 640 305 L 810 305 L 810 0 Z" fill="var(--orange-light)" opacity="0.55"/>
        <path class="accident-photo" role="img" aria-label="Photo of a black car with a crushed rear side after a road accident, trees behind"
              d="M724 0 L 1092 0 L 1092 305 L 802 305 C 760 210, 735 110, 724 0 Z"
              fill="url(#photo-tones)"/>
      </svg>
      <div class="message">
        <p class="firm-name">MARVELLA LAW FIRM P.C.</p>
        <h1 class="headline">CAR ACCIDENT?</h1>
        <a class="phone" href="tel:4075550148">(407) 555-0148</a>
      </div>
    </div>
  </div>
</body>
</html>
```